Bright Harbor; Teaching Series Art.

Our church is going to be teaching a series of messages under the topic/title: Bright Harbor. Just looking for a simple design to help with this. I have uploaded a design that is an example of what we were thinking.

The point of the design is to communicate a new way of doing things (given some of the impact of the coronavirus) - although the background doesn't need to be too busy - just something simple, clean and modern.

Even though it's for a church, we don't need any religious art in the background (crosses, people praying, etc.) Looking for a similar feel background to the one we uploaded.

The only text should be Bright Harbor and maybe highlighting the word Bright somehow.

Font styles to use
Sans Serif

Requirements
Must have
• Title of "Bright Harbor" - no other text.

```html
<!DOCTYPE html>
<html lang="en">
<head>
<meta charset="utf-8">
<title>Bright Harbor — Teaching Series</title>
<link rel="stylesheet" href="https://fonts.googleapis.com/css2?family=Lobster&family=Raleway:wght@500&display=swap">
<style>
  :root {
    --crimson-deep: #b51c24;
    --crimson: #d8222a;
    --scarlet: #e8392a;
    --orange: #ef6a32;
    --amber: #f4a05a;
    --peach: #f8c98e;
    --cream: #fdf0dc;
    --paper: #ffffff;
    --accent-yellow: #f7f06a;
    --title-white: #ffffff;
  }
  html, body {
    margin: 0;
    padding: 0;
    width: 1200px;
    height: 1199px;
    overflow: hidden;
    background: var(--paper);
  }
  .series-art {
    position: relative;
    width: 1200px;
    height: 1199px;
    overflow: hidden;
  }
  .wash-background {
    position: absolute;
    inset: 0;
    width: 1200px;
    height: 1199px;
    display: block;
  }
  .series-title {
    position: absolute;
    left: 0;
    top: 0;
    width: 1200px;
    margin: 0;
    font-weight: normal;
  }
  .title-highlight {
    position: absolute;
    left: 0;
    width: 1200px;
    top: 390px;
    text-align: center;
    transform: translateX(-26px);
    font-family: "Lobster", cursive;
    font-size: 134px;
    line-height: 1;
    color: var(--accent-yellow);
  }
  .title-main {
    position: absolute;
    left: 0;
    width: 1200px;
    top: 585px;
    text-align: center;
    transform: translateX(-4px);
    font-family: "Raleway", sans-serif;
    font-weight: 500;
    font-size: 140px;
    line-height: 1;
    letter-spacing: 4px;
    color: var(--title-white);
  }
</style>
</head>
<body>
  <main class="series-art">
    <svg class="wash-background" role="img" aria-label="Watercolour wash background in deep red, orange and peach fading to white at the bottom" viewBox="0 0 1200 1199" preserveAspectRatio="none">
      <defs>
        <linearGradient id="wash-base" x1="0" y1="0" x2="0" y2="1">
          <stop offset="0" stop-color="var(--crimson)"/>
          <stop offset="0.35" stop-color="var(--scarlet)"/>
          <stop offset="0.6" stop-color="var(--orange)"/>
          <stop offset="0.75" stop-color="var(--amber)"/>
          <stop offset="0.88" stop-color="var(--peach)"/>
          <stop offset="1" stop-color="var(--cream)"/>
        </linearGradient>
        <radialGradient id="wash-deep-right" cx="0.78" cy="0.2" r="0.45">
          <stop offset="0" stop-color="var(--crimson-deep)" stop-opacity="0.95"/>
          <stop offset="1" stop-color="var(--crimson-deep)" stop-opacity="0"/>
        </radialGradient>
        <radialGradient id="wash-deep-left" cx="0.05" cy="0.25" r="0.3">
          <stop offset="0" stop-color="var(--crimson-deep)" stop-opacity="0.8"/>
          <stop offset="1" stop-color="var(--crimson-deep)" stop-opacity="0"/>
        </radialGradient>
        <radialGradient id="wash-white-pool" cx="0.35" cy="1" r="0.4">
          <stop offset="0" stop-color="var(--paper)"/>
          <stop offset="0.6" stop-color="var(--paper)" stop-opacity="0.7"/>
          <stop offset="1" stop-color="var(--paper)" stop-opacity="0"/>
        </radialGradient>
        <radialGradient id="wash-peach-right" cx="0.85" cy="0.82" r="0.35">
          <stop offset="0" stop-color="var(--peach)" stop-opacity="0.8"/>
          <stop offset="1" stop-color="var(--peach)" stop-opacity="0"/>
        </radialGradient>
      </defs>
      <rect width="1200" height="1199" fill="url(#wash-base)"/>
      <rect width="1200" height="1199" fill="url(#wash-deep-right)"/>
      <rect width="1200" height="1199" fill="url(#wash-deep-left)"/>
      <rect width="1200" height="1199" fill="url(#wash-peach-right)"/>
      <rect width="1200" height="1199" fill="url(#wash-white-pool)"/>
    </svg>

    <h1 class="series-title">
      <span class="title-highlight">Bright</span>
      <span class="title-main">HARBOR</span>
    </h1>
  </main>
</body>
</html>
```